Clothing range for the petite modern mature woman needs a card design

We need a business card design for a new Sydney based company called river stone. We provide clothing to the modern mature woman who finds it difficult to source clothes that do not make them look frumpy or do not fit. We have an idea we would like an apple with the peel unravelling and possibly the silhouette of a woman's body coming out of the peel. The river stone represents the womans body shape and dressing it.

Target Market(s)

modern mature aged woman

Industry/Entity Type

Clothing

Contact Information for Business Card

abn: 42718063591
will provide email at a later date
a spiel re clothes for modern woman???

Font styles to use
Serif
Sans Serif

Requirements
Must have
• will need name - ABN -will need email address but still working on that (TBA)
Nice to have
• picture of an apple with its peel coming off and possibly the silhouette of a woman coming out. the issue a lot of women in the over 50 range have is that the clothing is very dated or makes the woman frumpy. we are providing clothes for the woman who has difficulty in finding fashionable clothes in their size.
Should not have
• don't want childlike

```html
<!DOCTYPE html>
<html lang="en">
<head>
<meta charset="utf-8">
<title>River Stone – Business Card</title>
<link href="https://fonts.googleapis.com/css2?family=Arimo:wght@400;700&display=swap" rel="stylesheet">
<style>
  :root {
    --backdrop: #8c8c8c;
    --card-light: #ececec;
    --card-dark: #353535;
    --band: #2f2f2f;
    --brand-green: #9dc41d;
    --leaf-light: #d4e84a;
    --leaf-deep: #8fbb1c;
    --ink: #222222;
    --icon: #4a4a4a;
  }
  * { margin: 0; padding: 0; box-sizing: border-box; }
  html, body { width: 1200px; height: 1000px; overflow: hidden; }
  body {
    background: var(--backdrop);
    font-family: "Arimo", Arial, sans-serif;
    position: relative;
  }
  .card {
    position: absolute;
    width: 700px;
    height: 400px;
    border-radius: 14px;
    overflow: hidden;
  }
  /* Front */
  .card-front {
    left: 90px; top: 70px;
    background: var(--card-light);
    border-top: 14px solid var(--band);
    border-bottom: 14px solid var(--band);
  }
  .artwork-area {
    position: absolute;
    left: 60px; top: 40px;
    width: 300px; height: 290px;
    border-radius: 40px;
    background: radial-gradient(circle at 55% 45%, var(--leaf-light), var(--leaf-deep));
  }
  .brand {
    position: absolute;
    right: 70px; top: 34px;
    text-align: left;
    color: var(--brand-green);
  }
  .brand-name {
    font-size: 30px;
    font-weight: 400;
    letter-spacing: 1px;
    text-transform: uppercase;
  }
  .brand-tagline {
    font-size: 13px;
    margin-top: 2px;
    padding-left: 8px;
  }
  .contact {
    position: absolute;
    right: 48px; top: 170px;
    text-align: right;
    color: var(--ink);
  }
  .person-name { font-size: 21px; margin-bottom: 28px; padding-right: 30px; }
  .contact-line {
    display: flex; align-items: center; justify-content: flex-end;
    gap: 10px;
    font-size: 17px;
    line-height: 26px;
  }
  .contact-line svg { width: 18px; height: 18px; }
  /* Back */
  .card-back {
    left: 410px; top: 520px;
    background: var(--card-dark);
    display: flex; align-items: center; justify-content: center;
  }
  .back-brand {
    color: var(--brand-green);
    font-size: 24px;
    letter-spacing: 1px;
    text-transform: uppercase;
  }
</style>
</head>
<body>
  <section class="card card-front">
    <div class="artwork-area" role="img" aria-label="Illustration of a green apple with its peel unravelling around a woman's silhouette"></div>

    <div class="brand">
      <div class="brand-name">River Stone</div>
      <div class="brand-tagline">Fashion for Modern Woman</div>
    </div>

    <div class="contact">
      <div class="person-name">Clara Jane Whitfield</div>
      <div class="contact-line">ABN&nbsp; 42718063591</div>
      <div class="contact-line">
        <svg viewBox="0 0 20 20" aria-hidden="true" fill="none" stroke="var(--icon)" stroke-width="1.4">
          <circle cx="10" cy="10" r="8"/>
          <ellipse cx="10" cy="10" rx="3.5" ry="8"/>
          <line x1="2" y1="10" x2="18" y2="10"/>
          <line x1="3.5" y1="5.5" x2="16.5" y2="5.5"/>
          <line x1="3.5" y1="14.5" x2="16.5" y2="14.5"/>
        </svg>
        www.riverstone.com
      </div>
      <div class="contact-line">
        <svg viewBox="0 0 20 20" aria-hidden="true" fill="none" stroke="var(--icon)" stroke-width="1.4">
          <rect x="2" y="4.5" width="16" height="11"/>
          <polyline points="2,4.5 10,11 18,4.5"/>
        </svg>
        riverstone@xmail.com
      </div>
    </div>
  </section>

  <section class="card card-back">
    <div class="back-brand">River Stone</div>
  </section>
</body>
</html>
```